Etiketten für Getränkedose (0,2 L)
Zielgruppe
Verkauf von Summerdrinks (Getränkedosen), stylisher Summerdrink (leicht alkoholhältig auf Rotwein basierend)
Aufgabenstellung
ich möchte eine Getränkedose (0,2 Liter wie Energydrink, etc.) designen lassen. Motiv ist etwas sommerliches, der Name ist olaGiardino welcher auf der Dose sein soll. Außerdem soll es vlt Paisley Muster und rote und gelbe Farbtöne enthalten (Giardino). Evtl. ein Bezug zu LGBT (rainbow logo) auch enthalten sein...
https://www.bildkammerfeld.de/de/search/paisley+rot hier meine Inspiration, kann aber auch etwas anders sein...

```html
<!DOCTYPE html>
<html lang="de">
<head>
<meta charset="utf-8">
<title>olaGiardino – Dosenetikett 0,2 L</title>
<link rel="stylesheet" href="https://fonts.googleapis.com/css2?family=Great+Vibes&family=Roboto+Condensed:wght@400;500&display=swap">
<style>
  :root {
    --page-bg: #ffffff;
    --label-text: #ffffff;
    --rose-orange: #f28a1e;
    --rose-yellow: #f5c518;
    --rose-green: #3aa84a;
    --rose-blue: #2f4fb8;
    --rose-purple: #7b2f9e;
    --rose-pink: #e0336f;
    --rose-dark: #1d1a22;
  }
  html, body {
    margin: 0;
    padding: 0;
    width: 1200px;
    height: 1200px;
    overflow: hidden;
    background: var(--page-bg);
  }
  .canvas {
    position: relative;
    width: 1200px;
    height: 1200px;
  }
  .can-label {
    position: absolute;
    left: 312px;
    top: 50px;
    width: 576px;
    height: 1100px;
    overflow: hidden;
  }
  .rose-photo {
    position: absolute;
    inset: 0;
    background:
      radial-gradient(circle at 20% 15%, var(--rose-blue) 0, transparent 30%),
      radial-gradient(circle at 45% 30%, var(--rose-orange) 0, transparent 25%),
      radial-gradient(circle at 85% 25%, var(--rose-orange) 0, transparent 22%),
      radial-gradient(circle at 10% 40%, var(--rose-green) 0, transparent 25%),
      radial-gradient(circle at 90% 60%, var(--rose-pink) 0, transparent 25%),
      radial-gradient(circle at 80% 75%, var(--rose-yellow) 0, transparent 25%),
      radial-gradient(circle at 25% 85%, var(--rose-orange) 0, transparent 30%),
      radial-gradient(circle at 15% 65%, var(--rose-green) 0, transparent 22%),
      radial-gradient(circle at 75% 95%, var(--rose-pink) 0, transparent 25%),
      radial-gradient(circle at 60% 10%, var(--rose-purple) 0, transparent 25%),
      var(--rose-dark);
  }
  .brand {
    position: absolute;
    left: 0;
    right: 0;
    top: 360px;
    color: var(--label-text);
    font-family: "Great Vibes", cursive;
  }
  .brand-sub {
    position: absolute;
    left: 230px;
    top: 0;
    font-size: 78px;
    line-height: 1;
    transform: rotate(-8deg);
  }
  .brand-name {
    position: absolute;
    left: 70px;
    top: 60px;
    font-size: 150px;
    line-height: 1;
  }
  .tagline {
    position: absolute;
    left: 185px;
    top: 625px;
    margin: 0;
    color: var(--label-text);
    font-family: "Roboto Condensed", sans-serif;
    font-weight: 500;
    font-size: 34px;
    letter-spacing: 4px;
  }
  .legal {
    position: absolute;
    left: 84px;
    right: 74px;
    bottom: 30px;
    display: flex;
    justify-content: space-between;
    align-items: baseline;
    color: var(--label-text);
    font-family: "Roboto Condensed", sans-serif;
  }
  .legal-note { font-size: 24px; }
  .legal-volume { font-size: 34px; }
</style>
</head>
<body>
  <main class="canvas">
    <section class="can-label">
      <div class="rose-photo" role="img" aria-label="Foto: dicht aneinanderliegende Regenbogenrosen in Orange, Gelb, Grün, Blau, Lila und Pink"></div>
      <div class="brand">
        <span class="brand-sub">ola</span>
        <span class="brand-name">Giardino</span>
      </div>
      <p class="tagline">SUMMERDRINK</p>
      <div class="legal">
        <span class="legal-note">alkoholhältig auf Rotwein basierend</span>
        <span class="legal-volume">0,2 L</span>
      </div>
    </section>
  </main>
</body>
</html>
```